Stainless Steel Water Bottle Packaging

We need a design for our cylindrical water bottle packaging.

Please see attached template (500ml cola bottle template .ai file) for exact dimensions.

VOLO is defined as the elemental forces of nature embodied in an object or person. The design should be eye catching and draw potential clients in. Although its a cylindrical bottle/box, the front which would face the customer when sitting on a shelf should clearly display our logo.

Requirements
Must have
• Designed to the specifications of the attached template (see attached)
• Our VOLO Logo (see attached) and website www.volobottle.com(in smaller font) must appear.
• Size of bottle must appear - '17 oz/500 ml'
• These should appear somewhere:
• 'INULATED DOUBLE-WALL STAINLESS STEEL WATER BOTTLE'
• 'VOLO Bottles magically keeps drinks cold for up to 24hrs, hot for 12',
• 'BPA Free'
• 'For every VOLO bottle purchased, a portion of proceeds will go towards charity. Each of our colour's have been assigned a specific charity. Please visit www.volobottle.com to find out which charity you helped support!'
• The Top circle - just our Symbol (flame/drop)
• The bottom circle - 'Inc. Designed in Canada made in China' on the outer edge leaving the middle empty for the UPC code.
• Reference website for the bottle case I'm looking for:
• http://shopcorventi.com/t-dune-lagoon-coral-insulated-water-bottle
Nice to have
• illustration of our water bottle shape (see attached) appearing somewhere on the box is something i had in mind but definitely not necessary.

```html
<!DOCTYPE html>
<html lang="en">
<head>
<meta charset="utf-8">
<title>VOLO Bottle Packaging Dieline</title>
<link rel="stylesheet" href="https://fonts.googleapis.com/css2?family=Oswald:wght@500;600&family=Roboto+Condensed:wght@400&family=Arimo:wght@400&family=Open+Sans:wght@400&family=Montserrat:wght@700&display=swap">
<style>
  :root {
    --sky: #2fa5de;
    --ocean: #0a5a98;
    --deep: #084d88;
    --gold: #f6c021;
    --white: #ffffff;
    --navy: #0d3f7c;
    --guide: #e0303a;
    --ink: #111111;
    --silver-light: #e4e2e4;
    --silver-dark: #9a98a0;
  }
  html, body {
    margin: 0;
    padding: 0;
    overflow: hidden;
    background: var(--white);
  }
  .canvas {
    width: 1006px;
    height: 1200px;
    position: relative;
    overflow: hidden;
    background: var(--white);
  }
  .canvas svg { display: block; }
  .spec-label {
    font-family: "Roboto Condensed", sans-serif;
    font-size: 38px;
    fill: var(--ink);
  }
  .dim-label {
    font-family: "Arimo", sans-serif;
    font-size: 18px;
    fill: var(--ink);
  }
  .dim-label--guide { fill: var(--guide); }
  .panel-type {
    font-family: "Oswald", sans-serif;
    font-weight: 500;
    fill: var(--white);
  }
  .panel-type--gold { fill: var(--gold); }
  .panel-type--navy { fill: var(--navy); font-weight: 600; }
  .brand-name {
    font-family: "Montserrat", sans-serif;
    font-weight: 700;
    fill: var(--white);
    letter-spacing: 6px;
  }
  .cap-text {
    font-family: "Open Sans", sans-serif;
    font-size: 10.5px;
    fill: var(--white);
  }
  .guide-line { stroke: var(--guide); stroke-width: 1; fill: none; }
  .dim-line { stroke: var(--ink); stroke-width: 1; fill: none; }
</style>
</head>
<body>
<div class="canvas">
<svg width="1006" height="1200" viewBox="0 0 1006 1200" xmlns="http://www.w3.org/2000/svg">
  <defs>
    <linearGradient id="panel-sky" x1="0" y1="0" x2="0" y2="1">
      <stop offset="0" stop-color="var(--sky)"/>
      <stop offset="1" stop-color="var(--ocean)"/>
    </linearGradient>
    <linearGradient id="panel-deep" x1="0" y1="0" x2="0" y2="1">
      <stop offset="0" stop-color="#0c62a4"/>
      <stop offset="1" stop-color="var(--deep)"/>
    </linearGradient>
    <linearGradient id="cap-fill" x1="0" y1="0" x2="0" y2="1">
      <stop offset="0" stop-color="#35aee3"/>
      <stop offset="1" stop-color="#0b5594"/>
    </linearGradient>
    <linearGradient id="metal-band" x1="0" y1="0" x2="1" y2="0">
      <stop offset="0" stop-color="var(--silver-light)"/>
      <stop offset="0.3" stop-color="var(--silver-dark)"/>
      <stop offset="0.55" stop-color="var(--silver-light)"/>
      <stop offset="0.8" stop-color="var(--silver-dark)"/>
      <stop offset="1" stop-color="var(--silver-light)"/>
    </linearGradient>
    <linearGradient id="gold-rule" x1="0" y1="0" x2="1" y2="0">
      <stop offset="0" stop-color="#f3c62a"/>
      <stop offset="0.5" stop-color="#fff1b0"/>
      <stop offset="1" stop-color="#f3c62a"/>
    </linearGradient>
    <path id="cap-arc-top" d="M 461 191 A 70 70 0 0 1 601 191"/>
    <path id="cap-arc-bottom" d="M 451 191 A 80 80 0 0 0 611 191"/>
  </defs>

  <!-- spec headings -->
  <text class="spec-label" x="74" y="56">cap’s diameter 7.8cm</text>
  <text class="spec-label" x="465" y="56">the bottom</text>

  <!-- top cap -->
  <g class="cap cap--top">
    <circle cx="319" cy="191" r="98" fill="url(#cap-fill)" stroke="var(--guide)" stroke-width="1"/>
    <text class="brand-name" x="319" y="202" font-size="30" text-anchor="middle" fill="var(--gold)" style="fill:var(--gold)">VOLO</text>
  </g>

  <!-- bottom cap -->
  <g class="cap cap--bottom">
    <circle cx="531" cy="191" r="98" fill="url(#cap-fill)" stroke="var(--guide)" stroke-width="1"/>
    <text class="cap-text"><textPath href="#cap-arc-top" startOffset="50%" text-anchor="middle">Inc. Designed in Canada</textPath></text>
    <text class="cap-text"><textPath href="#cap-arc-bottom" startOffset="50%" text-anchor="middle" side="right">Made in China</textPath></text>
    <circle cx="464" cy="191" r="6" class="guide-line"/>
    <circle cx="598" cy="191" r="6" class="guide-line"/>
  </g>

  <!-- wrap label -->
  <g class="wrap-label">
    <rect x="134" y="317" width="660" height="560" fill="url(#panel-sky)" role="img" aria-label="Soft hexagon pattern over blue gradient"/>
    <rect x="134" y="876" width="660" height="186" fill="url(#panel-deep)"/>

    <!-- metallic band -->
    <rect x="134" y="813" width="660" height="5" fill="url(#gold-rule)"/>
    <rect x="134" y="818" width="660" height="54" fill="url(#metal-band)"/>
    <rect x="134" y="872" width="660" height="5" fill="url(#gold-rule)"/>
    <text class="panel-type panel-type--navy" x="596" y="858" font-size="33" text-anchor="middle">WWW.VOLOBOTTLE.COM</text>

    <!-- brand -->
    <text class="brand-name" x="596" y="436" font-size="62" text-anchor="middle">VOLO</text>
    <text class="brand-name" x="598" y="680" font-size="58" text-anchor="middle" style="fill:var(--gold)">VOLO</text>

    <!-- keeps drinks -->
    <text class="panel-type" x="271" y="523" font-size="21" text-anchor="middle">VOLO BOTTLES MAGICALLY</text>
    <text class="panel-type" x="271" y="545" font-size="21" text-anchor="middle">KEEPS DRINKS</text>

    <g class="temp-icon temp-icon--cold" fill="none" stroke="var(--white)" stroke-width="4">
      <path d="M 208 588 A 22 22 0 0 1 243 572"/>
      <path d="M 249 590 A 22 22 0 0 1 236 610"/>
      <path d="M 203 582 l 5 9 l 6 -8" stroke-width="3"/>
      <g stroke-width="2"><path d="M 246 566 v 14 M 239 573 h 14 M 241 568 l 10 10 M 251 568 l -10 10"/></g>
      <text class="panel-type" x="201" y="614" font-size="17" stroke="none">24h</text>
    </g>
    <g class="temp-icon temp-icon--hot" fill="none" stroke="var(--white)" stroke-width="4">
      <path d="M 296 588 A 22 22 0 0 1 329 572"/>
      <path d="M 339 590 A 22 22 0 0 1 326 610"/>
      <path d="M 291 582 l 5 9 l 6 -8" stroke-width="3"/>
      <path d="M 336 582 c -7 -4 -5 -12 0 -18 c 2 5 7 7 5 13 c -1 3 -3 5 -5 5 z" fill="var(--gold)" stroke="none"/>
      <text class="panel-type panel-type--gold" x="290" y="614" font-size="17" stroke="none">12h</text>
    </g>

    <!-- charity box -->
    <rect x="176" y="636" width="191" height="163" rx="10" fill="none" stroke="var(--gold)" stroke-width="1.2"/>
    <g class="panel-type" font-size="12.5" text-anchor="middle">
      <text x="271" y="657" class="panel-type">FOR EVERY VOLO BOTTLE PURCHASED,</text>
      <text x="271" y="675" class="panel-type">A PORTION OF PROCEEDS WILL GO</text>
      <text x="271" y="693" class="panel-type">TOWARDS CHARITY. EACH OF OUR</text>
      <text x="271" y="711" class="panel-type">COLOUR’S HAVE BEEN ASSIGNED A</text>
      <text x="271" y="729" class="panel-type">SPECIFIC CHARITY. PLEASE VISIT</text>
      <text x="271" y="756" class="panel-type panel-type--gold" font-size="19">WWW.VOLOBOTTLE.COM</text>
      <text x="271" y="774" class="panel-type">TO FIND OUT WHICH CHARITY YOU</text>
      <text x="271" y="792" class="panel-type">HELPED SUPPORT!</text>
    </g>

    <!-- lower panel -->
    <g class="bpa" fill="none" stroke="var(--white)" stroke-width="2">
      <path d="M 204 974 C 206 950 222 936 243 929 C 242 952 230 968 210 970 Z"/>
      <path d="M 204 974 L 232 942"/>
    </g>
    <text class="panel-type panel-type--gold" x="247" y="966" font-size="26">BPA FREE</text>
    <text class="panel-type" x="596" y="921" font-size="17" text-anchor="middle">INULATED DOUBLE-WALL</text>
    <text class="panel-type" x="596" y="940" font-size="17" text-anchor="middle">STAINLESS STEEL WATER BOTTLE</text>
    <text class="panel-type" x="596" y="1012" font-size="31" text-anchor="middle">17 OZ/500 ML</text>

    <!-- guides -->
    <rect x="134" y="317" width="660" height="745" class="guide-line"/>
    <line x1="134" y1="342" x2="794" y2="342" class="guide-line"/>
    <line x1="159" y1="481" x2="794" y2="481" class="guide-line"/>
    <line x1="134" y1="1037" x2="794" y2="1037" class="guide-line"/>
    <line x1="159" y1="317" x2="159" y2="1062" stroke="#1c4d7c" stroke-width="1"/>
  </g>

  <!-- vertical dimensions -->
  <g class="dimensions dimensions--vertical">
    <line x1="76" y1="317" x2="76" y2="1062" class="dim-line"/>
    <line x1="66" y1="317" x2="88" y2="317" class="dim-line"/>
    <line x1="66" y1="342" x2="88" y2="342" class="dim-line"/>
    <line x1="66" y1="481" x2="88" y2="481" class="dim-line"/>
    <line x1="66" y1="1037" x2="88" y2="1037" class="dim-line"/>
    <line x1="66" y1="1062" x2="88" y2="1062" class="dim-line"/>
    <rect x="66" y="385" width="20" height="70" fill="var(--white)"/>
    <rect x="66" y="720" width="20" height="92" fill="var(--white)"/>
    <text class="dim-label dim-label--guide" x="39" y="338">10.00mm</text>
    <text class="dim-label" transform="translate(82 412) rotate(-90)" text-anchor="middle">55.00mm</text>
    <text class="dim-label" transform="translate(83 766) rotate(-90)" text-anchor="middle">220.00mm</text>
    <text class="dim-label dim-label--guide" x="39" y="1058">10.00mm</text>
  </g>

  <!-- horizontal dimensions -->
  <g class="dimensions dimensions--horizontal">
    <line x1="134" y1="1101" x2="794" y2="1101" class="dim-line"/>
    <line x1="134" y1="1088" x2="134" y2="1114" class="dim-line"/>
    <line x1="159" y1="1088" x2="159" y2="1114" class="dim-line"/>
    <line x1="794" y1="1088" x2="794" y2="1114" class="dim-line"/>
    <text class="dim-label" x="98" y="1131">10.00mm</text>
    <text class="dim-label" x="481" y="1133" text-anchor="middle">8X3.14159=251.327mm</text>
  </g>

  <!-- spec footer -->
  <text class="spec-label" x="22" y="1189">diameter 8cm</text>
  <text class="spec-label" x="286" y="1189">the whole height 27.5cm</text>
  <text class="spec-label" x="714" y="1189">cap’s height 5.5cm</text>
</svg>
</div>
</body>
</html>
```